New to ArtHarbor? This contest is for you!

Are you new to ArtHarbor and looking to enter your first contest? Look no further!

We're launching this special contest to help you get started on building a design portfolio at ArtHarbor!

Requirements:
Create a mini one-page portfolio featuring selection of 3-5 designs from your personal portfolio to sell yourself as a designer.

The submission (1 page portfolio) should showcase your design skills to our design quality team and to our designers.

We've mocked up a few layouts to provide a guide for how to layout your submission. Please see the attachments to the brief. (This is a guide only.)

The mini portfolio should grab attention and communicate who your personal design brand.

Designers are limited to 1 design submission, so show us your best work!

You must upload your entry before 12:00am 1 Oct 2016 UTC

This must be your very FIRST entry on ArtHarbor to be eligible to receive a prize. If you've already entered other ArtHarbor contests you won't be eligible to win the prizes.

Your design must adhere to our quality standards and be approved by our quality team to be eligible to receive a prize.

Target Market(s)

ArtHarbor quality team
ArtHarbor customers

Industry/Entity Type

Graphic Design

Requirements
Must have
• Showcase 3-5 of your best designs from your personal work on 1 page.
• The portfolio should grab our judges attention and communicate who you are as a designer.
Nice to have
• Text or descriptions about the work is optional
Should not have
• No individual design examples should be submitted.

```html
<!DOCTYPE html>
<html lang="en">
<head>
<meta charset="utf-8">
<title>Rami .T — Portfolio</title>
<link href="https://fonts.googleapis.com/css2?family=Montserrat:wght@400;500;600&family=Raleway:ital,wght@0,400;0,500;0,600;1,400&display=swap" rel="stylesheet">
<style>
:root{
  --ink:#1c1c1e;
  --ink-deep:#111112;
  --paper:#ffffff;
  --mist:#f3f3f3;
  --cyan:#00bff3;
  --text:#555a60;
  --muted:#9a9ea3;
  --line:#3a3a3d;
}
*{margin:0;padding:0;box-sizing:border-box}
html,body{width:1200px;height:1200px;overflow:hidden;background:var(--paper)}
body{position:relative;font-family:"Raleway",sans-serif;color:var(--text)}
.abs{position:absolute}
.page{position:absolute;left:315px;top:0;width:570px;height:1200px}

/* header */
.brand{left:116px;top:5px;font-family:"Montserrat",sans-serif;font-size:9px;letter-spacing:2px;color:var(--ink);font-weight:500}
.brand-sub{left:116px;top:15px;font-size:4.4px;color:var(--ink)}
.nav{left:310px;top:10px;display:flex;gap:13px;font-family:"Montserrat",sans-serif;font-size:3.6px;letter-spacing:.3px;color:#666}
.nav .active{color:var(--cyan)}

/* hero */
.hero{left:0;top:26px;width:570px;height:215px;background:var(--ink)}
.hero-kicker{left:0;top:74px;width:570px;text-align:center;font-style:italic;font-size:4px;color:#fff;letter-spacing:.2px}
.hero-title{left:0;top:90px;width:570px;text-align:center;font-family:"Montserrat",sans-serif;font-weight:500;font-size:14px;color:#fff;letter-spacing:.5px}
.btn{top:120px;height:17px;width:59px;font-family:"Montserrat",sans-serif;font-size:4px;letter-spacing:1px;color:#fff;display:flex;align-items:center;justify-content:center}
.btn-ghost{left:221px;border:1px solid #fff}
.btn-solid{left:290px;background:var(--cyan)}
.hero-arrow{left:280px;top:202px}

/* history */
.mist{left:0;top:241px;width:570px;height:526px;background:var(--mist)}
.section-title{width:570px;left:0;text-align:center;font-family:"Montserrat",sans-serif;font-size:7px;letter-spacing:.4px;color:var(--ink)}
.divider{left:270px;width:30px;height:5px}
.copy{left:179px;width:212px;text-align:center;font-size:4.2px;line-height:6.2px;color:var(--text)}
.strip{left:0;top:398px;width:570px;height:165px;display:flex}
.shot{flex:1;height:165px}

/* service cards */
.card{top:606px;width:110px;height:118px;background:#fff;padding:0 18px}
.card svg{display:block;margin:18px auto 0}
.card .rule{width:9px;height:1px;background:var(--cyan);margin:7px auto 0}
.card h3{font-family:"Montserrat",sans-serif;font-weight:500;font-size:4.4px;letter-spacing:1.3px;text-align:center;color:var(--ink);margin-top:6px}
.card p{font-size:3.4px;line-height:4.8px;margin-top:6px}
.card ul{list-style:none;font-size:3.4px;line-height:4.8px;margin-top:4px}

/* clients */
.quote{left:184px;top:839px;width:202px;text-align:center;font-size:4.2px;line-height:6.2px;color:var(--text)}
.quote-by{left:0;top:864px;width:570px;text-align:center;font-size:3.6px;color:var(--muted)}
.client{top:907px;width:86px;height:24px;display:flex;align-items:center;justify-content:center;gap:4px;font-family:"Montserrat",sans-serif;font-weight:600;font-size:7px;color:#7b8188}
.client .dot{width:6px;height:6px;border-radius:50%;background:#7b8188}

/* footer */
.dark{left:0;top:980px;width:570px;height:182px;background:var(--ink-deep)}
.panel{top:996px;width:170px;height:149px;border:1px solid var(--line)}
.panel h4{font-family:"Montserrat",sans-serif;font-weight:400;font-size:6.6px;color:#fff;text-align:center;margin-top:26px;letter-spacing:.3px}
.panel .rule{width:8px;height:1px;background:var(--cyan);margin:9px auto 0}
.panel p{color:#fff;font-size:3.6px;line-height:5.8px;text-align:center;padding:0 22px;margin-top:12px}
.field{left:20px;width:128px;font-family:"Montserrat",sans-serif;font-size:3.6px;color:#fff;letter-spacing:.3px;border-bottom:1px solid var(--line)}
.send{right:20px;top:120px;font-family:"Montserrat",sans-serif;font-size:3.8px;color:var(--cyan);letter-spacing:.5px}
.bar{left:0;top:1162px;width:570px;height:38px;background:var(--cyan)}
.copyright{left:112px;top:17px;font-size:3.4px;color:#fff}
.social{left:418px;top:16px;display:flex;gap:8px;font-size:3.4px;color:#fff}
</style>
</head>
<body>
<div class="page">

  <header>
    <div class="abs brand">Rami .T</div>
    <div class="abs brand-sub">Front-end Developer, Graphic Designer &amp; Videographer</div>
    <nav class="abs nav">
      <span class="active">HOME</span><span>PORTFOLIO</span><span>SERVICES</span><span>CLIENTS</span><span>CONTACT</span>
    </nav>
  </header>

  <section class="abs hero">
    <div class="abs hero-kicker">DESIGN / DEVELOPMENT / VIDEOGRAPHY</div>
    <h1 class="abs hero-title">CREATIVITY HAVE NEW LEVEL</h1>
    <div class="abs btn btn-ghost">WORK</div>
    <div class="abs btn btn-solid">HIRE ME</div>
    <svg class="abs hero-arrow" width="10" height="7" viewBox="0 0 10 7"><path d="M1 1h8L5 6z" fill="none" stroke="#00bff3" stroke-width=".9"/></svg>
  </section>

  <section class="abs mist"></section>
  <h2 class="abs section-title" style="top:282px">LITTLE HISTORY</h2>
  <svg class="abs divider" style="top:302px" viewBox="0 0 30 5"><line x1="0" y1="2.5" x2="30" y2="2.5" stroke="#00bff3" stroke-width=".7"/><path d="M15 .5l2 2-2 2-2-2z" fill="#f3f3f3" stroke="#00bff3" stroke-width=".6"/></svg>
  <div class="abs copy" style="top:318px">
    I am a devoted individual with over 7 years of experience in professional responsive web designing and web development services based on frameworks of PHP, HTML5, CSS3 etc. I've got a vast portfolio of my creative and out of the box custom web designs. I design to give your website an attractive and an appealing look for sure.<br>I'm well equipped with the latest web technologies.
  </div>
  <div class="abs copy" style="top:355px">
    My immense experience of professional web designing and development services has undoubtedly made me an expert of my field. Be it projects designed for PressKit, Jambula, Open Source, Magnetra, OpenTill etc I've mastered them all.<br>In short, I am proficient with professional responsive web designing and development services.
  </div>

  <div class="abs strip">
    <div class="shot" role="img" aria-label="Website screenshot: sports campaign landing page" style="background:linear-gradient(180deg,#8a4a3e 0,#8a4a3e 33%,#1d56b0 33%,#1d56b0 64%,#7dbb3c 64%,#7dbb3c 80%,#1d56b0 80%)"></div>
    <div class="shot" role="img" aria-label="Website screenshot: security camera product site" style="background:linear-gradient(180deg,#d9d9db 0,#eeeeee 45%,#f7f7f7 70%,#cfcfcf 100%)"></div>
    <div class="shot" role="img" aria-label="Website screenshot: fashion gallery with video section" style="background:linear-gradient(180deg,#f4f1ee 0,#d8b9b2 20%,#c9a39a 55%,#f4f1ee 76%,#1c1c1c 78%,#5a3d35 100%)"></div>
    <div class="shot" role="img" aria-label="Website screenshot: apparel shop product grid" style="background:linear-gradient(180deg,#f5f5f5 0,#c77a5a 35%,#9a4a5c 65%,#e8e3e0 100%)"></div>
    <div class="shot" role="img" aria-label="Website screenshot: travel agency deals page" style="background:linear-gradient(180deg,#ffffff 0,#4e88c4 14%,#8db7d6 30%,#ffffff 34%,#e46a3c 55%,#f2d2c4 78%,#ffffff 100%)"></div>
    <div class="shot" role="img" aria-label="Website screenshot: community organisation site" style="background:linear-gradient(180deg,#1a3c94 0,#2445a3 10%,#7a5a44 20%,#1f43a6 30%,#1f43a6 100%)"></div>
  </div>

  <article class="abs card" style="left:111px">
    <svg width="14" height="14" viewBox="0 0 14 14"><path d="M3 11l1-3 6-6 2 2-6 6zM9 3l2 2M3 11l3-1" fill="none" stroke="#333" stroke-width=".8"/></svg>
    <div class="rule"></div><h3>IDEA</h3>
    <p>The most impressive websites and app experiences are rooted in smart design, embody clear vision and are backed by the right technology.</p>
    <ul><li>&gt;&gt; Website Design</li><li>&gt;&gt; Web Application Design</li><li>&gt;&gt; Information Architecture</li><li>&gt;&gt; Digital Strategy</li><li>&gt;&gt; Copywriting</li><li>&gt;&gt; Search Optimization (SEO)</li></ul>
  </article>
  <article class="abs card" style="left:230px">
    <svg width="14" height="14" viewBox="0 0 14 14"><rect x="2" y="2" width="6" height="9" fill="none" stroke="#333" stroke-width=".8"/><rect x="6" y="5" width="6" height="7" fill="none" stroke="#333" stroke-width=".8"/><path d="M4 1v2M6 1v2M1 5h2M1 7h2" stroke="#333" stroke-width=".7"/></svg>
    <div class="rule"></div><h3>WORK</h3>
    <p>Best-in-class digital projects require technology that perfectly supports the design. We rely on the right tools for the job, not a one-size-fits-all tech stack.</p>
    <ul><li>&gt;&gt; Front and Backend Web Development</li><li>&gt;&gt; Mobile App Development</li><li>&gt;&gt; API Integrations</li><li>&gt;&gt; Shopping &amp; E-Commerce Integration</li><li>&gt;&gt; Content Management Systems (CMS)</li><li>&gt;&gt; Forge CMS Development</li><li>&gt;&gt; PressKit</li></ul>
  </article>
  <article class="abs card" style="left:349px">
    <svg width="14" height="14" viewBox="0 0 14 14"><rect x="2" y="2" width="10" height="7" fill="none" stroke="#333" stroke-width=".8"/><path d="M7 9v2M4 12h6" stroke="#333" stroke-width=".8"/></svg>
    <div class="rule"></div><h3>DELIVER</h3>
    <p>With the site tested and ready to go, I upload it to your web server and do any required configuration, including set up of plugins and modules for content management systems, and installing Seekly Analytics or any other tracking software.</p>
    <p>Finally, I submit your completed website to the three major search engines: Seekly, Findr and Yodel including an XML sitemap and a robots.txt file.</p>
  </article>

  <h2 class="abs section-title" style="top:814px">MY CLIENTS ARE</h2>
  <svg class="abs divider" style="top:828px" viewBox="0 0 30 5"><line x1="0" y1="2.5" x2="30" y2="2.5" stroke="#00bff3" stroke-width=".7"/><path d="M15 .5l2 2-2 2-2-2z" fill="#fff" stroke="#00bff3" stroke-width=".6"/></svg>
  <p class="abs quote">He always answered after minutes, understood every single - complicated thing I requested. The landing page I offered got million times better than I imagined it. For real he is so far the best web designer you can get. Animations, videos and difficult design was no problem.</p>
  <div class="abs quote-by">Mr. Harlan</div>

  <div class="abs client" style="left:114px">NORTHLINE</div>
  <div class="abs client" style="left:200px"><span class="dot"></span>GUARDWELL</div>
  <div class="abs client" style="left:285px">K&amp;L</div>
  <div class="abs client" style="left:370px"><span class="dot"></span>HILLBLOOM</div>

  <footer>
    <div class="abs dark"></div>
    <div class="abs panel" style="left:111px">
      <h4>ABOUT ME</h4><div class="rule"></div>
      <p>My immense experience of professional web designing and development services has undoubtedly made me an expert of my field. Be it projects designed for PressKit, Jambula, Open Source, Magnetra, OpenTill etc I've mastered them all.<br>In short, I am proficient with professional responsive web designing and development services.</p>
    </div>
    <div class="abs panel" style="left:289px">
      <h4>CONTACT ME</h4>
      <div class="abs field" style="top:41px;height:14px">EMAIL</div>
      <div class="abs field" style="top:72px;height:17px">MESSAGE</div>
      <div class="abs field" style="top:96px;height:11px"></div>
      <div class="abs send">SEND</div>
    </div>
    <div class="abs bar">
      <div class="abs copyright">© 2016 - Rami .T</div>
      <div class="abs social"><span>Link</span><span>Feed</span><span>Shots</span></div>
    </div>
  </footer>

</div>
</body>
</html>
```